Cobalt Mirak PPT 1

I need a PPT template that I could apply to several uses both internally and externally.
Cobalt Mirak is not a new company but rather a new spin-off from my previous brand. We are a Business Consulting firm known for our ability implement the advice we provide our clients and see it through to fruition. The vast majority of our projects involve IT or software technology. Particularly with new software implementations, software integrations arising from a merger or acquisition. We consult to almost every industry except Mining, construction and agriculture but mostly for Financial Services, automotive and Hospitality services. We offer a tailored service through trusted, longstanding relationships with our clients.
From a look, feel and overall theme perspective, Mirak is the Viking god of war but, more importantly, he is known for his WISDOM, ADAPATABILITY, RESILENCE. He is in fact a shape shifter. We chose Mirak because we advise our clients on ways to remain Agile and adaptable to rapidly changing environments to remain competitive now and in the future.
The word steel was added to denote strength, reliability sustainability.
I have recently run a logo design competition for the new logo.

I would like an all-purpose PPT template that is crisp, clean, uncomplicated but professional and attractive to the eye.
I am keen to see some ideas.
Thanks
Dale

```html
<!DOCTYPE html>
<html lang="en">
<head>
<meta charset="utf-8">
<title>Cobalt Mirak – Presentation Template</title>
<link rel="stylesheet" href="https://fonts.googleapis.com/css2?family=Montserrat:ital,wght@0,400;0,500;0,600;0,700;0,800;1,600&display=swap">
<style>
:root{
  --red:#d0121b;
  --red-deep:#a80c12;
  --ink:#3a3a3c;
  --grey-title:#7b7b7d;
  --grey-text:#8a8a8c;
  --grey-light:#e6e6e7;
  --dark:#2a2a2c;
  --stage:#88898d;
  --white:#ffffff;
}
*{box-sizing:border-box;margin:0;padding:0}
html,body{width:1200px;height:2296px;overflow:hidden;background:var(--stage)}
body{font-family:"Montserrat",sans-serif;color:var(--ink)}
.canvas{position:relative;width:1200px;height:2296px;background:var(--stage);overflow:hidden}
.slide{position:absolute;width:439px;height:246px;background:var(--white);overflow:hidden;box-shadow:0 4px 14px rgba(0,0,0,.25)}
.col-l{left:149px}.col-r{left:612px}
.row1{top:105px}.row2{top:368px}.row3{top:631px}.row4{top:893px}
.row5{top:1156px}.row6{top:1419px}.row7{top:1682px}.row8{top:1945px}
.abs{position:absolute}
.title{position:absolute;left:22px;top:6px;font-weight:800;font-size:19px;line-height:1.15;color:var(--grey-title);letter-spacing:.4px}
.rule{position:absolute;left:0;height:1px;background:var(--red)}
.rule::after{content:"";position:absolute;right:-3px;top:-3px;width:7px;height:7px;border-radius:50%;background:var(--red)}
.brand{position:absolute;right:14px;top:10px;font-weight:700;font-size:9px;line-height:1.05;color:var(--grey-title);text-align:left;letter-spacing:.6px}
.pg{position:absolute;right:8px;bottom:6px;width:16px;height:16px;border-radius:50%;background:var(--dark);color:#fff;font-size:6.5px;font-weight:600;display:flex;align-items:center;justify-content:center}
.body{font-size:7px;line-height:1.7;color:var(--grey-text);text-align:justify}
.art{position:absolute}
.tiny{font-size:4.2px;line-height:1.6;color:var(--grey-text);text-align:center}

/* cover */
.cover{background:radial-gradient(ellipse at 60% 80%,#4a4a4d 0%,#222224 55%,#151516 100%)}
.cover .brand-big{position:absolute;left:38px;top:52px;font-weight:800;font-size:31px;line-height:1;color:#c9c9cc;letter-spacing:1px}
.cover .tag{position:absolute;left:39px;top:153px;font-weight:800;font-size:19px;line-height:1.35;color:#fff}
.red{color:var(--red)}

/* agenda */
.agenda-list{position:absolute;left:103px;top:52px;list-style:none}
.agenda-list li{display:flex;align-items:center;height:35.2px;font-size:8.5px;font-weight:500;color:var(--ink)}
.num{width:20px;height:20px;border-radius:50%;background:var(--red);color:#fff;font-size:7px;font-weight:700;display:flex;align-items:center;justify-content:center;margin-right:14px;box-shadow:0 0 0 2px #f1d4d5}

/* features */
.feat{position:absolute;font-size:7px;line-height:1.6;color:var(--ink);text-align:center;font-weight:500}
.ico{position:absolute;width:32px;height:32px;border-radius:50%;display:flex;align-items:center;justify-content:center}
.ico.r{background:var(--red)}.ico.g{background:#8f8f91}

/* why */
.why-circle{position:absolute;left:244px;top:44px;width:170px;height:170px;border-radius:50%;background:var(--red);border:4px solid #fff;box-shadow:0 0 0 2px var(--red),0 4px 10px rgba(0,0,0,.2);color:#fff;font-size:7.3px;line-height:1.45;text-align:center;display:flex;align-items:center;justify-content:center;padding:22px}

/* team cards */
.team{position:absolute;left:19px;top:71px;display:flex;gap:3px}
.card{width:77px}
.card-head{height:73px;background:#f3f3f3;border:1px solid #e0e0e0;display:flex;flex-direction:column;align-items:center;padding-top:8px}
.card-head.active{background:#8e8e90}
.avatar{width:38px;height:38px;border-radius:50%;background:linear-gradient(160deg,#6a6a6d,#2e2e30);border:2px solid #fff}
.card-name{font-size:5.5px;font-weight:700;margin-top:5px;color:var(--ink)}
.card-head.active .card-name{color:#fff}
.card-role{font-size:4px;color:var(--ink)}
.card .tiny{margin-top:6px;padding:0 3px}

/* quote */
.quote{background:linear-gradient(120deg,#b4b4b6 0%,#9a9a9c 60%,#8f8f91 100%)}
.quote p{position:absolute;left:96px;top:96px;width:258px;font-size:10px;font-style:italic;font-weight:600;line-height:1.6;color:#fff;text-align:center}
.qmark{position:absolute;font-size:34px;font-weight:800;color:var(--red);line-height:1}

/* timeline */
.tl-label{position:absolute;font-size:4.8px;font-weight:700;text-align:center;line-height:1.35;color:var(--ink);width:80px}

/* infographics */
.box{position:absolute;top:86px;width:98px;height:136px;border:2px solid #bdbdbf;border-radius:14px;text-align:center;padding-top:10px}
.box h4{font-size:7px;font-weight:600;color:var(--red);margin:6px 0 4px}
.box .tiny{text-align:justify;padding:0 10px}

/* thank you dark */
.thanks-dark{background:linear-gradient(135deg,#7a7a7d 0%,#4b4b4e 100%)}
.thanks-dark .brand-big{position:absolute;left:0;right:0;top:52px;text-align:center;font-weight:800;font-size:31px;color:#fff;letter-spacing:1px;line-height:1}
.thanks-dark .ty{position:absolute;left:0;right:0;top:147px;text-align:center;font-weight:800;font-size:29px;color:#fff}
.contact-band{position:absolute;left:34px;right:14px;bottom:0;height:19px;background:var(--red);border-radius:10px 10px 0 0;color:#fff;font-size:7px;font-weight:600;display:flex;align-items:center;justify-content:center;gap:8px}

/* what we do */
.wwd-item{position:absolute;font-size:6px;line-height:1.4;color:#f2f2f2}
.wwd-item b{display:block;font-size:7.2px;margin-bottom:3px;color:#fff}
.wwd-item.right{color:var(--grey-text)}
.wwd-item.right b{color:var(--ink)}
.wicon{position:absolute;width:22px;height:22px;border-radius:50%;display:flex;align-items:center;justify-content:center}

/* red thank you */
.thanks-red{background:linear-gradient(120deg,#d8161d 0%,#c80f16 60%,#b70d13 100%)}
.thanks-red .brand-r{position:absolute;left:26px;top:16px;font-weight:800;font-size:20px;color:#fff;opacity:.9;line-height:1}
.thanks-red .ty{position:absolute;left:19px;top:66px;font-weight:800;font-size:20px;color:#fff}
.c-list{position:absolute;left:25px;top:118px;list-style:none}
.c-list li{display:flex;align-items:center;height:26.5px;font-size:7.5px;color:#fff;font-weight:500}
.c-dot{width:18px;height:18px;border-radius:50%;background:#fff;margin-right:14px;display:flex;align-items:center;justify-content:center}
</style>
</head>
<body>
<main class="canvas">

<!-- Row 1 left: cover -->
<section class="slide col-l row1 cover">
  <div class="brand-big">COBALT<br>MIRAK</div>
  <div class="rule" style="left:40px;top:137px;width:245px"></div>
  <h1 class="tag">WISDOM, <span class="red">ADAPATABILITY</span><br>RESILENCE</h1>
</section>

<!-- Row 1 right: features -->
<section class="slide col-r row1">
  <h2 class="title">FEATURES &amp;<br>BENEFITS</h2>
  <div class="rule" style="top:60px;width:160px"></div>
  <div class="art" role="img" aria-label="Stylised silver and dark wing illustration with red orb" style="left:170px;top:0;width:269px;height:246px;background:linear-gradient(160deg,#ffffff 0%,#d9d9db 30%,#3a3a3d 60%,#d5d5d7 100%);clip-path:ellipse(72% 62% at 78% 44%)"></div>
  <div class="brand">COBALT<br>MIRAK</div>
  <p class="feat" style="left:16px;top:86px;width:156px">Nemo enim ipsam voluptatem quia voluptas sit aspernatur aut odit aut fugit, sed quia consequuntur magni dolores eos qui ratione</p>
  <div class="ico r" style="left:164px;top:86px"><svg width="14" height="12" viewBox="0 0 14 12"><rect x="1" y="1" width="12" height="8" fill="none" stroke="#fff" stroke-width="1.6"/><rect x="5" y="10" width="4" height="1.5" fill="#fff"/></svg></div>
  <p class="feat" style="left:66px;top:149px;width:140px">Nemo enim ipsam voluptatem quia voluptas sit aspernatur aut odit aut fugit, sed quia consequuntur</p>
  <div class="ico g" style="left:212px;top:148px"><svg width="14" height="14" viewBox="0 0 24 24"><path d="M12 2l3 7 7 .5-5.5 4.5 2 7.5L12 17l-6.5 4.5 2-7.5L2 9.5 9 9z" fill="#fff"/></svg></div>
  <p class="feat" style="left:150px;top:205px;width:140px">Nemo enim ipsam voluptatem quia voluptas sit aspernatur aut</p>
  <div class="ico r" style="left:322px;top:198px"><svg width="12" height="14" viewBox="0 0 12 14"><path d="M1 1h7l3 3v9H1z" fill="#fff"/></svg></div>
  <div class="pg">09</div>
</section>

<!-- Row 2 left: agenda -->
<section class="slide col-l row2">
  <h2 class="title">AGENDA</h2>
  <div class="rule" style="top:37px;width:128px"></div>
  <div class="brand">COBALT<br>MIRAK</div>
  <ol class="agenda-list">
    <li><span class="num">01</span>LOREM IPSUM DOLOR SIT</li>
    <li><span class="num">02</span>LOREM IPSUM DOLOR SIT AMET, CONSECTETEA</li>
    <li><span class="num">03</span>LOREM IPSUM DOLOR SIT</li>
    <li><span class="num">04</span>LOREM IPSUM DOLOR SIT AMET, CONSECTETEA</li>
    <li><span class="num">05</span>LOREM IPSUM DOLOR SIT</li>
  </ol>
  <div class="pg">02</div>
</section>

<!-- Row 2 right: meet our team -->
<section class="slide col-r row2">
  <div class="art" role="img" aria-label="Photo of two consultants reviewing charts at a laptop" style="left:190px;top:0;width:249px;height:105px;background:linear-gradient(120deg,#d6d6d8 0%,#8a90a0 45%,#2f3a55 70%,#cfd0d3 100%);clip-path:polygon(8% 0,100% 0,100% 100%,30% 100%)"></div>
  <div class="art" role="img" aria-label="Grey wing illustration with red orb" style="left:180px;top:110px;width:259px;height:136px;background:radial-gradient(circle at 62% 52%,#d0121b 0 22px,#f4f4f4 23px,#bcbcbe 55%,#6d6d70 80%,#ffffff 100%)"></div>
  <h2 class="title" style="top:58px">MEET OUR<br><span style="color:#6b6b6d">TEAM</span></h2>
  <div class="rule" style="top:112px;width:160px"></div>
  <div class="brand">COBALT<br>MIRAK</div>
  <p class="body" style="position:absolute;left:16px;top:130px;width:172px">Nemo enim ipsam voluptatem quia voluptas sit aspernatur aut odit aut fugit, sed quia consequuntur magni dolores eos qui ratione voluptatem sequi nesciunt. Neque porro quisquam est, qui dolorem ipsum quia dolor sit amet, consectetur, adipisci velit, sed quia non numquam eius modi tempora incidunt ut labore et dolore magnam</p>
  <div class="pg">10</div>
</section>

<!-- Row 3 left: about us -->
<section class="slide col-l row3">
  <div class="art" role="img" aria-label="Dark and silver wing illustration with red orb" style="left:170px;top:0;width:269px;height:246px;background:linear-gradient(160deg,#ffffff 0%,#dcdcde 25%,#2e2e31 55%,#cfcfd1 100%);clip-path:ellipse(70% 60% at 78% 44%)"></div>
  <h2 class="title">ABOUT US</h2>
  <div class="rule" style="top:37px;width:146px"></div>
  <div class="brand">COBALT<br>MIRAK</div>
  <p class="body" style="position:absolute;left:22px;top:54px;width:145px">Nemo enim ipsam voluptatem quia voluptas sit aspernatur aut odit aut fugit, sed quia consequuntur magni dolores eos qui ratione voluptatem sequi nesciunt. Neque porro quisquam est, qui dolorem ipsum quia dolor sit amet, consectetur, adipisci velit, sed quia non numquam eius modi tempora incidunt ut labore et dolore magnam aliquam quaerat voluptatemt enim ad minima veniam, quis nostrum exercitationem ullam corporis suscipit laboriosam.</p>
  <div class="pg">03</div>
</section>

<!-- Row 3 right: problem statement -->
<section class="slide col-r row3">
  <h2 class="title" style="left:16px">PROBLEM STATEMENT</h2>
  <div class="rule" style="top:45px;width:264px"></div>
  <div class="brand">COBALT<br>MIRAK</div>
  <div class="abs" style="left:22px;top:95px;font-weight:800;font-size:29px;line-height:1;color:#8d8d90;letter-spacing:1px">COBALT<br>MIRAK</div>
  <div class="body" style="position:absolute;left:207px;top:68px;width:208px">
    <p>Nemo enim ipsam voluptatem quia voluptas sit aspernatur aut odit aut fugit, sed quia consequuntur magni dolores eos qui ratione voluptatem sequi nesciunt. Neque porro quisquam est, qui dolorem ipsum quia dolor sit amet, consectetur, adipisci velit, sed quia non numquam eius modi tempora incidunt ut labore et dolore magnam</p>
    <p style="margin-top:10px">Nemo enim ipsam voluptatem quia voluptas sit aspernatur aut odit aut fugit, sed quia consequuntur magni dolores eos qui ratione voluptatem sequi nesque porro quisqolorem ipsum quia dolor</p>
  </div>
  <div class="pg">11</div>
</section>

<!-- Row 4 left: why choose us -->
<section class="slide col-l row4">
  <h2 class="title">WHY CHOOSE US</h2>
  <div class="rule" style="top:37px;width:229px"></div>
  <div class="brand">COBALT<br>MIRAK</div>
  <p class="body" style="position:absolute;left:22px;top:54px;width:190px">Nemo enim ipsam voluptatem quia voluptas sit aspernatur aut odit aut fugit, sed quia consequuntur magni dolores eos qui ratione voluptatem sequi nesciunt. Neque porro quisquam est, qui dolorem ipsum quia dolor sit amet, consectetur, adipisci velit, sed quia non numquam eius modi tempora incidunt ut labore et dolore magnam aliquam quaerat voluptatemt enim ad minima veniam, quis nostrum exercitationem ullam corpuscipit laboriosamnisi ut aliquidcommodi consequatuauis autem vel eum iure reprehenderit qui in ea voluptate velit esse quam nihil molestiae consequatur</p>
  <div class="why-circle">Nemo enim ipsam voluptatem quia voluptas sit aspernatur aut odit aut fugit, sed quia consequuntur magni dolores eos qui ratione voluptatem sequi nesciunt. Neque porro quisquam est, qui dolorem ipsum quia dolor sit amet, consectetur, adipisci velit, sed quia non numquam eius modi tempora</div>
  <div class="pg">04</div>
</section>

<!-- Row 4 right: our team -->
<section class="slide col-r row4">
  <h2 class="title" style="left:16px">OUR TEAM</h2>
  <div class="rule" style="top:45px;width:130px"></div>
  <div class="brand">COBALT<br>MIRAK</div>
  <div class="team">
    <div class="card"><div class="card-head"><div class="avatar" role="img" aria-label="Portrait of Marcus Hale"></div><div class="card-name">Marcus Hale</div><div class="card-role">Project Leader</div></div><p class="tiny">Lorem ipsum dolor sit amet, consectetur adipiscing elit, sed do eiusmod tempor incididunt ut labore et dolore magna aliqua.</p></div>
    <div class="card"><div class="card-head"><div class="avatar" role="img" aria-label="Portrait of Dr Nora Pike"></div><div class="card-name">Dr Nora Pike</div></div><p class="tiny">Lorem ipsum dolor sit amet, consectetur adipiscing elit, sed do eiusmod tempor incididunt ut labore et dolore magna aliqua.</p></div>
    <div class="card"><div class="card-head active"><div class="avatar" role="img" aria-label="Portrait of Owen Ashby"></div><div class="card-name">Owen Ashby</div></div><p class="tiny">Lorem ipsum dolor sit amet, consectetur adipiscing elit, sed do eiusmod tempor incididunt ut labore et dolore magna aliqua.</p></div>
    <div class="card"><div class="card-head"><div class="avatar" role="img" aria-label="Portrait of Felix Moran"></div><div class="card-name">Felix Moran</div></div><p class="tiny">Lorem ipsum dolor sit amet, consectetur adipiscing elit, sed do eiusmod tempor incididunt ut labore et dolore magna aliqua.</p></div>
    <div class="card"><div class="card-head"><div class="avatar" role="img" aria-label="Portrait of Leah Carver"></div><div class="card-name">Leah Carver</div></div><p class="tiny">Lorem ipsum dolor sit amet, consectetur adipiscing elit, sed do eiusmod tempor incididunt ut labore et dolore magna aliqua.</p></div>
  </div>
  <div class="pg">12</div>
</section>

<!-- Row 5 left: quote -->
<section class="slide col-l row5 quote">
  <div class="qmark" style="left:69px;top:58px">“</div>
  <div class="abs" style="left:79px;top:82px;width:2px;height:95px;background:var(--red)"></div>
  <div class="abs" style="left:79px;top:175px;width:102px;height:2px;background:var(--red)"></div>
  <p>“Lorem ipsum dolor sit amet, consectetur adipiscing elit, sed do eiusmod tempor incididunt ut labore et dolore magna alt eminim veniam”</p>
  <div class="qmark" style="left:186px;top:165px">”</div>
</section>

<!-- Row 5 right: timeline -->
<section class="slide col-r row5">
  <h2 class="title" style="left:16px">TIMELINE</h2>
  <div class="rule" style="top:45px;width:130px"></div>
  <div class="brand">COBALT<br>MIRAK</div>
  <div class="tl-label" style="left:75px;top:60px">Project Commences<br>Dec 24</div>
  <div class="tl-label" style="left:176px;top:60px">Inception &amp; v:<br>Dec 2023- Jan 2024</div>
  <div class="tl-label" style="left:279px;top:57px">Stakeholder Engagement<br>Jan 2023 - Feb 2024</div>
  <div class="tl-label" style="left:126px;top:200px">Development of Draft Plan<br>Feb-Mar 2024</div>
  <div class="tl-label" style="left:227px;top:200px">Final Report<br>Mar -Apr 2024</div>
  <svg class="abs" style="left:0;top:0" width="439" height="246" viewBox="0 0 439 246">
    <g stroke="#555" stroke-width="1">
      <line x1="115" y1="78" x2="115" y2="110"/><line x1="216" y1="78" x2="216" y2="110"/><line x1="319" y1="78" x2="319" y2="110"/>
      <line x1="166" y1="162" x2="166" y2="195"/><line x1="267" y1="162" x2="267" y2="195"/>
    </g>
    <g fill="#555"><circle cx="115" cy="78" r="2"/><circle cx="216" cy="78" r="2"/><circle cx="319" cy="78" r="2"/><circle cx="166" cy="195" r="2"/><circle cx="267" cy="195" r="2"/></g>
    <g>
      <circle cx="115" cy="136" r="26" fill="#e4e4e5"/><path d="M89 136 A26 26 0 0 1 141 136" fill="var(--red)"/><circle cx="115" cy="136" r="20" fill="#fff"/>
      <circle cx="166" cy="136" r="26" fill="#e4e4e5"/><path d="M140 136 A26 26 0 0 0 192 136" fill="#9a9a9c"/><circle cx="166" cy="136" r="20" fill="#fff"/>
      <circle cx="216" cy="136" r="26" fill="#e4e4e5"/><path d="M190 136 A26 26 0 0 1 242 136" fill="var(--red)"/><circle cx="216" cy="136" r="20" fill="#fff"/>
      <circle cx="267" cy="136" r="26" fill="#e4e4e5"/><path d="M241 136 A26 26 0 0 0 293 136" fill="#9a9a9c"/><circle cx="267" cy="136" r="20" fill="#fff"/>
      <circle cx="319" cy="136" r="26" fill="#e4e4e5"/><path d="M293 136 A26 26 0 0 1 345 136" fill="var(--red)"/><circle cx="319" cy="136" r="20" fill="#fff"/>
    </g>
    <g fill="none" stroke="var(--red)" stroke-width="1.2">
      <circle cx="115" cy="136" r="7"/><circle cx="115" cy="136" r="3"/>
      <rect x="158" y="128" width="16" height="16"/><line x1="161" y1="133" x2="171" y2="133"/><line x1="161" y1="138" x2="171" y2="138"/>
      <rect x="208" y="128" width="13" height="16"/><circle cx="220" cy="141" r="4"/>
      <rect x="259" y="128" width="16" height="16"/><polyline points="261,141 265,136 269,139 273,132"/>
      <circle cx="314" cy="131" r="2.5"/><circle cx="324" cy="131" r="2.5"/><rect x="310" y="137" width="18" height="6"/>
    </g>
  </svg>
  <div class="pg">13</div>
</section>

<!-- Row 6 left: graph -->
<section class="slide col-l row6">
  <h2 class="title">OUR GRAPH</h2>
  <div class="rule" style="top:37px;width:182px"></div>
  <div class="brand">COBALT<br>MIRAK</div>
  <p class="body" style="position:absolute;left:22px;top:52px;width:395px">Nemo enim ipsam voluptatem quia voluptas sit aspernatur aut odit aut fugit, sed quia consequuntur magni dolores eos qui ratione voluptatem sequi nesciunt. Neque porro quisquam est, qui dolorem ipsum quia dolor sit amet, consectetur, adipisci velit, sed quia non numquam eius</p>
  <svg class="abs" style="left:0;top:0" width="439" height="246" viewBox="0 0 439 246">
    <g font-size="4" fill="#777" text-anchor="end" font-family="Montserrat,sans-serif">
      <text x="50" y="107">120</text><text x="50" y="124">100</text><text x="50" y="141">80</text><text x="50" y="158">60</text><text x="50" y="175">40</text><text x="50" y="192">20</text><text x="50" y="209">0</text>
    </g>
    <g fill="#e2e2e3">
      <rect x="64" y="105" width="15" height="102"/><rect x="103" y="105" width="15" height="102"/><rect x="142" y="105" width="15" height="102"/><rect x="181" y="105" width="15" height="102"/><rect x="220" y="105" width="15" height="102"/><rect x="259" y="105" width="15" height="102"/><rect x="298" y="105" width="15" height="102"/><rect x="337" y="105" width="15" height="102"/><rect x="376" y="105" width="15" height="102"/>
    </g>
    <rect x="64" y="190" width="15" height="17" fill="#2e2e30"/>
    <rect x="103" y="164" width="15" height="43" fill="#3a3a3c"/>
    <rect x="142" y="156" width="15" height="51" fill="#3a3a3c"/>
    <rect x="181" y="181" width="15" height="26" fill="#2e2e30"/>
    <rect x="220" y="139" width="15" height="68" fill="var(--red)"/>
    <rect x="259" y="130" width="15" height="77" fill="#3a3a3c"/>
    <rect x="298" y="181" width="15" height="26" fill="#3a3a3c"/>
    <rect x="337" y="122" width="15" height="85" fill="#2e2e30"/>
    <rect x="376" y="147" width="15" height="60" fill="#3a3a3c"/>
    <g font-size="4" fill="#fff" text-anchor="middle" font-family="Montserrat,sans-serif">
      <text x="71.5" y="204">20%</text><text x="110.5" y="204">50%</text><text x="149.5" y="204">60%</text><text x="188.5" y="204">30%</text><text x="227.5" y="204">60%</text><text x="266.5" y="204">90%</text><text x="305.5" y="204">30%</text><text x="344.5" y="204">100%</text><text x="383.5" y="204">70%</text>
    </g>
  </svg>
  <div class="pg">06</div>
</section>

<!-- Row 6 right: reporting -->
<section class="slide col-r row6">
  <h2 class="title" style="left:16px">REPORTING</h2>
  <div class="rule" style="top:45px;width:145px"></div>
  <div class="brand">COBALT<br>MIRAK</div>
  <div class="body" style="position:absolute;left:15px;top:58px;width:195px;font-size:6.4px;line-height:1.6">
    <p>Lorem ipsum dolor sit amet, consectetur adipiscing elit, sed do eiusmod tempor incididunt ut labore et dolore magna aliqua. Ut enim ad minim veniam, quis nostrud exercitation ullamco laboris nisi ut aliquip ex ea</p>
    <p style="margin-top:8px">Sed ut perspiciatis unde omnis iste natus error sit voluptatem accusantium doloremque laudantium, totam rem aperiam, eaque ipsa quae ab illo inventore veritatis et quasi architecto beatae vitae dicta sunt explicabo. Nemo enim ipsam voluptatem quia voluptas sit aspernatur aut odit aut fugit, sed quia consequuntur magni dolores eos qui ratione voluptatem sequi nesciunt. Neque porro quisquam est, qui dolorem ipsum quia dolor sit amet.</p>
  </div>
  <svg class="abs" style="left:200px;top:40px" width="239" height="175" viewBox="0 0 239 175">
    <g transform="translate(72,88)">
      <path d="M0 0 L0 -70 A70 70 0 0 1 49.5 -49.5 Z" fill="var(--red)"/>
      <path d="M0 0 L49.5 -49.5 A70 70 0 0 1 70 0 Z" fill="#a8a8aa"/>
      <path d="M0 0 L70 0 A70 70 0 0 1 49.5 49.5 Z" fill="var(--red)"/>
      <path d="M0 0 L49.5 49.5 A70 70 0 0 1 0 70 Z" fill="#8f8f91"/>
      <circle r="47" fill="#fff" stroke="#ececec" stroke-width="2"/>
      <text x="0" y="3" text-anchor="middle" font-size="8" font-weight="700" fill="#333" font-family="Montserrat,sans-serif">REPORTING</text>
      <g font-size="5" fill="#fff" font-weight="600" font-family="Montserrat,sans-serif">
        <text x="13" y="-56">Task 1:</text><text x="43" y="-25">Task 2:</text><text x="43" y="23">Task 3:</text><text x="15" y="55">Task 4:</text>
      </g>
    </g>
    <g font-size="5" fill="#333" font-weight="600" font-family="Montserrat,sans-serif">
      <text x="95" y="20">Inception Situation</text><text x="95" y="26">Analysis</text>
      <text x="112" y="56">Traditional Owner &amp;</text><text x="112" y="62">Stakeholder Consultation</text>
      <text x="114" y="107">Utilisation Strategy</text><text x="114" y="113">Development &amp; Draft Plan</text>
      <text x="94" y="150">Reporting</text>
    </g>
  </svg>
  <div class="pg">14</div>
</section>

<!-- Row 7 left: infographics -->
<section class="slide col-l row7">
  <h2 class="title" style="left:16px">OUR INFOGRAPHICS</h2>
  <div class="rule" style="top:37px;width:245px"></div>
  <div class="brand">COBALT<br>MIRAK</div>
  <p class="body" style="position:absolute;left:22px;top:50px;width:395px">Nemo enim ipsam voluptatem quia voluptas sit aspernatur aut odit aut fugit, sed quia consequuntur magni dolores eos qui rationm quia dolor sit amet, consectesquia non numquam eius</p>
  <div class="box" style="left:48px">
    <svg width="10" height="14" viewBox="0 0 10 14"><rect x="1" y="0" width="8" height="14" rx="1.5" fill="var(--red)"/></svg>
    <h4>TITLE HERE</h4><p class="tiny">Lorem ipsum dolor sit amet, consectetur adipiscing elit, sed do eiusmodtempor incididunt ut labore et dolore magna aliqua. Ut enim ad minim veniam quis nostrud exercitation ullamco.</p>
  </div>
  <div class="box" style="left:166px">
    <svg width="16" height="14" viewBox="0 0 16 14"><rect x="1" y="1" width="14" height="9" fill="none" stroke="var(--red)" stroke-width="2"/><rect x="5" y="11" width="6" height="2" fill="var(--red)"/></svg>
    <h4>TITLE HERE</h4><p class="tiny">Lorem ipsum dolor sit amet, consectetur adipiscing elit, sed do eiusmodempor incididunt ut labore et dolore magna aliqua. Ut enim ad minim veniam quis nostrud exercitation ullamco.</p>
  </div>
  <div class="box" style="left:293px">
    <svg width="20" height="14" viewBox="0 0 20 14"><path d="M4 13a4 4 0 0 1 0-8 6 6 0 0 1 11 1 3.5 3.5 0 0 1 1 7z" fill="var(--red)"/></svg>
    <h4>TITLE HERE</h4><p class="tiny">Lorem ipsum dolor sit amet, consectetur adipiscing elit, sed do eiusmodempor incididunt ut labore et dolore magna aliqua. Ut enim ad minim veniam quis nostrud exercitation ullamco.</p>
  </div>
  <svg class="abs" style="left:0;top:0" width="439" height="246" viewBox="0 0 439 246">
    <g fill="none" stroke="#bdbdbf" stroke-width="2">
      <path d="M146 160 Q158 150 158 140 L164 140"/>
      <path d="M264 160 Q276 150 280 140 L288 140"/><path d="M283 135 L289 140 L283 145"/>
    </g>
  </svg>
  <div class="pg">07</div>
</section>

<!-- Row 7 right: thank you (dark) -->
<section class="slide col-r row7 thanks-dark">
  <div class="brand-big">COBALT<br>MIRAK</div>
  <div class="rule" style="left:96px;top:123px;width:245px"></div>
  <h2 class="ty">THANK <span class="red">YOU</span></h2>
  <div class="contact-band">
    <span>☎ Call Us : +1 555 010 0199</span><span>|</span><span>✉ hello@cobaltmirak.example</span>
  </div>
</section>

<!-- Row 8 left: what we do -->
<section class="slide col-l row8">
  <div class="art" role="img" aria-label="Dark grey gradient panel with faint dotted texture" style="left:0;top:0;width:245px;height:246px;background:linear-gradient(180deg,#3a3a3d 0%,#6f6f72 60%,#a5a5a7 100%);clip-path:path('M0 0 L230 0 Q255 60 238 125 Q222 190 235 246 L0 246 Z')"></div>
  <svg class="abs" style="left:0;top:0" width="439" height="246" viewBox="0 0 439 246"><path d="M230 0 Q255 60 238 125 Q222 190 235 246" fill="none" stroke="#555" stroke-width="2"/></svg>
  <h2 class="title" style="left:16px;color:#fff">WHAT WE DO</h2>
  <div class="rule" style="top:37px;width:208px"></div>
  <div class="brand">COBALT<br>MIRAK</div>
  <div class="wicon" style="left:29px;top:57px;background:#fff"><svg width="9" height="10" viewBox="0 0 9 10"><rect x="1" y="4" width="7" height="6" fill="none" stroke="#777"/><path d="M2.5 4V2.5a2 2 0 0 1 4 0V4" fill="none" stroke="#777"/></svg></div>
  <div class="wwd-item" style="left:62px;top:57px;width:140px"><b>Voluptatum deleniti</b>Voluptatum deleniti atque corrupti quos dolores et quas molestias excepturi sint occaecati</div>
  <div class="wicon" style="left:29px;top:114px;background:var(--red)"><svg width="10" height="10" viewBox="0 0 10 10"><path d="M2 8 L7 3 L8 4 L3 9 L1.5 9.5Z" fill="#fff"/></svg></div>
  <div class="wwd-item" style="left:62px;top:113px;width:140px"><b>Raesentium volupt</b>Voluptatum deleniti atque corrupti quos dolores et quas molestias epturi sint occaecati cupiditate non</div>
  <div class="wicon" style="left:29px;top:174px;background:#fff"><svg width="8" height="10" viewBox="0 0 8 10"><path d="M1 1h4l2 2v6H1z" fill="none" stroke="#777"/></svg></div>
  <div class="wwd-item" style="left:62px;top:174px;width:140px"><b>Raesentium volupt</b>Voluptatum deleniti atque corrupti quos dolores et quas molestias xcepturi sint occaecati</div>
  <div class="wicon" style="left:232px;top:50px;background:var(--red)"><svg width="8" height="10" viewBox="0 0 8 10"><ellipse cx="4" cy="2" rx="3" ry="1.5" fill="#fff"/><rect x="1" y="2" width="6" height="6" fill="#fff"/></svg></div>
  <div class="wwd-item right" style="left:265px;top:48px;width:150px"><b>Raesentium volupt</b>Voluptatum deleniti atque corrupti quos dolores et quas molestias excepturi sint occaecati cupiditate non provident,</div>
  <div class="wicon" style="left:219px;top:111px;background:#8f8f91"><svg width="10" height="10" viewBox="0 0 10 10"><circle cx="5" cy="3" r="2" fill="none" stroke="#fff"/><path d="M1 9.5a4 4 0 0 1 8 0" fill="none" stroke="#fff"/></svg></div>
  <div class="wwd-item right" style="left:254px;top:110px;width:155px"><b>Raesentium volupt</b>Voluptatum deleniti atque corrupti quos dolores et quas molestias excepturi sint occaecati cupiditate non provident,</div>
  <div class="wicon" style="left:205px;top:170px;background:var(--red)"><svg width="10" height="9" viewBox="0 0 10 9"><rect x="1" y="1" width="8" height="5" fill="none" stroke="#fff"/><rect x="3.5" y="7" width="3" height="1.5" fill="#fff"/></svg></div>
  <div class="wwd-item right" style="left:236px;top:170px;width:155px"><b>Raesentium volupt</b>Voluptatum deleniti atque corrupti quos dolores et quas molestias excepturi sint occaecati cupiditate non provident,</div>
  <div class="pg">08</div>
</section>

<!-- Row 8 right: thank you (red) -->
<section class="slide col-r row8 thanks-red">
  <div class="art" role="img" aria-label="Faint office photo overlay with silver wing and white orb" style="left:235px;top:60px;width:190px;height:140px;background:radial-gradient(circle at 72% 58%,#ffffff 0 12px,#c9c9cb 14px,#8a8a8d 40%,rgba(200,15,22,0) 70%)"></div>
  <div class="brand-r">COBALT<br>MIRAK</div>
  <h2 class="ty">THANK YOU</h2>
  <div class="rule" style="top:100px;width:155px;background:#fff"></div>
  <ul class="c-list">
    <li><span class="c-dot"><svg width="8" height="8" viewBox="0 0 10 10"><path d="M2 1l2 2-1 1.5a6 6 0 0 0 2.5 2.5L7 6l2 2-1.5 1.5C4 9 1 6 .5 2.5z" fill="var(--red)"/></svg></span>+1 (555) 010 0199</li>
    <li><span class="c-dot"><svg width="8" height="6" viewBox="0 0 8 6"><rect width="8" height="6" fill="var(--red)"/><path d="M0 0l4 3 4-3" fill="none" stroke="#fff" stroke-width=".8"/></svg></span>info@cobaltmirak.example</li>
    <li><span class="c-dot"><svg width="7" height="9" viewBox="0 0 7 9"><path d="M3.5 9S0 5 0 3.5a3.5 3.5 0 0 1 7 0C7 5 3.5 9 3.5 9z" fill="var(--red)"/><circle cx="3.5" cy="3.5" r="1.2" fill="#fff"/></svg></span>212 Harbor Lane, Portland, United States</li>
    <li><span class="c-dot"><svg width="8" height="8" viewBox="0 0 8 8"><circle cx="4" cy="4" r="3.5" fill="none" stroke="var(--red)"/><path d="M.5 4h7M4 .5c-2 2-2 5 0 7M4 .5c2 2 2 5 0 7" fill="none" stroke="var(--red)" stroke-width=".7"/></svg></span>www.cobaltmirak.example</li>
  </ul>
</section>

</main>
</body>
</html>
```